Real Estate Website

We have a an existing website - harborkeyhomes.com.au which we want redesigned.

We want it to look more like the design/style of https://www.stallworth.com.au/

```html
<!DOCTYPE html>
<html lang="en">
<head>
<meta charset="utf-8">
<title>Harborkey Estate Agents</title>
<link href="https://fonts.googleapis.com/css2?family=Raleway:wght@300;400;600&family=Roboto:wght@400;500;700&display=swap" rel="stylesheet">
<style>
:root{
  --teal:#178797;
  --teal-dark:#0f6f7d;
  --navy:#0d2d40;
  --ink:#222;
  --muted:#666;
  --icon:#9a9a9a;
  --line:#e4e4e4;
  --star:#f2b705;
}
*{box-sizing:border-box;margin:0;padding:0}
html,body{width:1200px;height:4843px;overflow:hidden}
body{font-family:"Roboto",sans-serif;color:var(--ink);background:#fff;position:relative}
.abs{position:absolute}
h2.section-title{position:absolute;left:0;width:1200px;text-align:center;font-family:"Raleway",sans-serif;font-weight:400;font-size:33px;letter-spacing:.5px;color:#222;text-transform:uppercase}

/* header + hero */
.hero{position:absolute;top:0;left:0;width:1200px;height:604px;background:linear-gradient(115deg,#4b4f55 0%,#8c8f93 40%,#c9c7c2 70%,#a9a49d 100%)}
.topbar{position:absolute;top:0;left:0;width:1200px;height:53px;background:rgba(13,45,64,.85)}
.brand{position:absolute;left:110px;top:15px;color:#fff;font-family:"Roboto",sans-serif;font-size:20px;font-weight:700;display:flex;align-items:center;gap:10px}
.brand i{display:block;width:18px;height:18px;background:#fff}
.nav{position:absolute;left:412px;top:19px;display:flex;gap:22px;font-size:13px;font-weight:500;color:#fff}
.top-phone{position:absolute;right:110px;top:17px;color:#fff;font-weight:700;font-size:16px;display:flex;gap:8px;align-items:center}
.hero h1{position:absolute;left:107px;top:210px;width:560px;color:#fff;font-family:"Raleway",sans-serif;font-weight:400;font-size:30px;line-height:39px}
.hero p{position:absolute;left:107px;top:306px;width:480px;color:#fff;font-size:13px;font-weight:500;line-height:27px}
.search{position:absolute;display:flex;height:46px}
.search .field{background:#fff;width:345px;height:46px;font-size:14px;color:#777;padding:15px 16px}
.search .go{background:var(--teal);color:#fff;font-size:13px;font-weight:700;padding:15px 16px;border:2px solid #fff;text-transform:uppercase}
.play{position:absolute;left:816px;top:263px;width:75px;height:75px;border-radius:50%;background:rgba(255,255,255,.85)}

/* service cards */
.svc{position:absolute;top:718px;width:233px;height:211px;border:2px solid #e6e6e6;border-radius:8px;background:#fff;text-align:center}
.svc.active{border-color:var(--teal);box-shadow:0 4px 14px rgba(0,0,0,.12)}
.svc .ico{width:110px;height:110px;margin:28px auto 0;border-radius:50%}
.svc span{display:block;margin-top:22px;font-weight:700;font-size:16px;text-transform:uppercase}

/* listings */
.listing{position:absolute;top:1155px;width:478px;height:342px;border-radius:8px;overflow:hidden}
.listing .tag{position:absolute;right:14px;top:16px;background:var(--teal);color:#fff;font-size:12px;font-weight:700;padding:9px 14px;text-transform:uppercase}
.listing h3{position:absolute;left:40px;top:254px;color:#fff;font-size:14px;font-weight:700;text-transform:uppercase}
.listing .addr{position:absolute;left:40px;top:285px;color:#fff;font-size:13px;display:flex;gap:10px;align-items:center}

/* testimonials */
.reviews{position:absolute;top:1642px;left:0;width:1200px;height:593px;background:linear-gradient(180deg,#eef0f1,#e6e9eb)}
.badge{position:absolute;top:1800px;width:130px;height:50px;border-radius:6px;background:#d7dadd}
.quote{position:absolute;left:233px;top:1898px;width:732px;height:256px;background:#fff;border-radius:6px;box-shadow:0 4px 16px rgba(0,0,0,.1);text-align:center}
.quote .stars{margin-top:34px;color:var(--star);font-size:14px;letter-spacing:1px}
.quote h4{margin-top:16px;font-size:13px;font-weight:700}
.quote p{margin:20px 40px 0;font-size:14px;line-height:26px;color:var(--muted)}
.quote .who{margin-top:22px;color:var(--teal);font-weight:700;font-size:13px}

/* recent sales */
.sale{position:absolute;top:2425px;width:320px;height:406px;border:1px solid var(--line);border-radius:8px;overflow:hidden;background:#fff;box-shadow:0 2px 8px rgba(0,0,0,.06)}
.sale .head{height:46px;background:var(--teal);color:#fff;font-size:12px;font-weight:700;text-align:center;padding-top:16px;text-transform:uppercase}
.sale .photo{height:183px}
.sale .price{margin:32px 0 0 22px;color:var(--teal);font-weight:700;font-size:19px}
.sale .loc{margin:20px 30px 0 22px;font-size:13px;line-height:22px;color:var(--muted);display:flex;gap:12px}
.sale .feat{margin:18px 0 0 22px;display:flex;gap:28px;font-size:13px;font-weight:700;color:#333}
.sale .feat span{display:flex;align-items:center;gap:14px}
.arrow-btn{position:absolute;top:2616px;width:30px;height:30px;border-radius:50%;border:1px solid #ccc;background:#fff}

/* cta */
.cta{position:absolute;top:2970px;left:0;width:1200px;height:318px;background:linear-gradient(180deg,#1b93a3,#127d8c)}
.cta h2{position:absolute;left:0;top:70px;width:1200px;text-align:center;color:#fff;font-family:"Raleway",sans-serif;font-weight:400;font-size:33px;line-height:45px;text-transform:uppercase}

/* news */
.news{position:absolute;top:3478px;width:318px}
.news .photo{height:218px}
.news h3{margin:32px 0 0 12px;font-size:13px;font-weight:700;line-height:23px;text-transform:uppercase}
.news .meta{position:absolute;top:335px;left:18px;display:flex;gap:30px;font-size:12px;color:var(--muted)}
.news .meta span{display:flex;align-items:center;gap:8px}

/* contact */
.contact{position:absolute;top:3969px;left:0;width:1200px;height:467px;background:linear-gradient(180deg,#1a91a1,#117b8a)}
.contact h2{position:absolute;left:0;top:68px;width:1200px;text-align:center;color:#fff;font-weight:700;font-size:38px;text-transform:uppercase}
.input{position:absolute;background:#fff;border-radius:3px;font-size:14px;color:#777;padding:16px 16px}
.submit{position:absolute;left:523px;top:336px;width:154px;height:46px;background:var(--navy);color:#fff;font-size:13px;font-weight:700;text-align:center;padding-top:15px;border-radius:3px}

/* footer */
.footer{position:absolute;top:4436px;left:0;width:1200px;height:348px;background:var(--navy);color:#fff}
.footer h5{position:absolute;font-size:13px;font-weight:700;text-transform:uppercase}
.footer .row{position:absolute;left:107px;display:flex;align-items:center;gap:22px;font-size:13px;line-height:21px}
.circle{width:32px;height:32px;border-radius:50%;background:#fff;flex:none;display:flex;align-items:center;justify-content:center}
.links{position:absolute;left:423px;top:110px;list-style:none;font-size:13px;line-height:34px}
.links li::before{content:"»";margin-right:14px}
.hours{position:absolute;left:592px;top:112px;font-size:13px;line-height:30px}
.hours div{display:flex}
.hours b{font-weight:400;width:110px}
.map{position:absolute;left:832px;top:86px;width:263px;height:222px;background:linear-gradient(135deg,#eef0f2,#dfe4e8)}
.copy{position:absolute;top:4784px;left:0;width:1200px;height:59px;background:var(--teal);color:#fff;font-size:13px;text-align:center;padding-top:22px}
</style>
</head>
<body>

<section class="hero">
  <div role="img" aria-label="Photo of a smiling couple viewing a bright modern kitchen" style="position:absolute;inset:0"></div>
  <header class="topbar">
    <div class="brand"><i></i>Harborkey</div>
    <nav class="nav"><span>Home</span><span>Buying</span><span>Selling</span><span>Renting</span><span>Blog</span><span>About Us</span><span>Contact Us</span></nav>
    <div class="top-phone"><svg width="14" height="14" viewBox="0 0 24 24"><path fill="#fff" d="M6.6 10.8a15 15 0 006.6 6.6l2.2-2.2c.3-.3.7-.4 1-.2 1.1.4 2.3.6 3.6.6.6 0 1 .4 1 1V20c0 .6-.4 1-1 1A17 17 0 013 4c0-.6.4-1 1-1h3.5c.6 0 1 .4 1 1 0 1.3.2 2.5.6 3.6.1.3 0 .7-.2 1z"/></svg>02 9000 4821</div>
  </header>
  <h1>Full service property management improving your investment returns</h1>
  <p>Harborkey Estate Agency is driven by a passionate, hardworking, caring team who are your friends in real estate.</p>
  <div class="search" style="left:107px;top:386px"><div class="field" style="width:350px">Search by Suburb</div><div class="go">Check Location</div></div>
  <div class="play"><svg width="75" height="75" viewBox="0 0 75 75"><circle cx="37.5" cy="37.5" r="24" fill="var(--teal)"/><path d="M32 27l15 10.5L32 48z" fill="#fff"/></svg></div>
</section>

<div class="svc" style="left:107px"><div class="ico" role="img" aria-label="Illustration of apartment buildings" style="background:#d9edf1"></div><span>Property Alert</span></div>
<div class="svc" style="left:357px"><div class="ico" role="img" aria-label="Illustration of an agent with a house badge" style="background:#f6e2c7"></div><span>Market Appraisal</span></div>
<div class="svc active" style="left:607px"><div class="ico" role="img" aria-label="Illustration of a team of three" style="background:#fadcd3"></div><span>Our Team</span></div>
<div class="svc" style="left:857px"><div class="ico" role="img" aria-label="Illustration of an envelope and phone" style="background:#fde7d2"></div><span>Contact Us</span></div>

<h2 class="section-title" style="top:1063px">Featured Listings</h2>
<div class="listing" style="left:113px">
  <div role="img" aria-label="Photo of a modern apartment living room" style="position:absolute;inset:0;background:linear-gradient(180deg,#c9c8c4,#6f6c68)"></div>
  <div class="tag">For Sale $749,000</div>
  <h3>Modern Apartment!!</h3>
  <div class="addr"><svg width="10" height="13" viewBox="0 0 14 18"><path d="M7 0a7 7 0 017 7c0 5-7 11-7 11S0 12 0 7a7 7 0 017-7z" fill="var(--teal)"/></svg>607/24 Marlow Street For Sale in WOLLI C</div>
</div>
<div class="listing" style="left:609px">
  <div role="img" aria-label="Photo of a renovated studio with city views" style="position:absolute;inset:0;background:linear-gradient(180deg,#a8b2b8,#4d5255)"></div>
  <div class="tag">Contact Agent</div>
  <h3>Newly Renovated Studio in Excellent Location</h3>
  <div class="addr"><svg width="10" height="13" viewBox="0 0 14 18"><path d="M7 0a7 7 0 017 7c0 5-7 11-7 11S0 12 0 7a7 7 0 017-7z" fill="var(--teal)"/></svg>11/14 Ferris Park Road For Rent in QU</div>
</div>

<section class="reviews"></section>
<h2 class="section-title" style="top:1714px">What Our Customers Say</h2>
<div class="badge" style="left:356px"></div>
<div class="badge" style="left:540px"></div>
<div class="badge" style="left:718px"></div>
<svg class="abs" style="left:156px;top:2015px" width="32" height="20"><path d="M30 10H4M11 3L3 10l8 7" stroke="var(--teal)" stroke-width="3" fill="none"/></svg>
<svg class="abs" style="left:1012px;top:2015px" width="32" height="20"><path d="M2 10h26M21 3l8 7-8 7" stroke="var(--teal)" stroke-width="3" fill="none"/></svg>
<div class="quote">
  <div class="stars">★★★★★</div>
  <h4>RE: 18 LINDEN STREET, BARDWELL VALLEY.</h4>
  <p>We would like to thank Leo Tran for his professionalism and efficiency during the sale of our house. We met Leo Tran and we knew right away he was the person to sell our house. Leo was honest and personable and made some great suggestions prior to listing the house to attract more buyers.</p>
  <div class="who">DEAR LEO</div>
</div>

<h2 class="section-title" style="top:2333px">Recent Sales</h2>
<div class="arrow-btn" style="left:32px"><svg width="28" height="28"><path d="M16 9l-5 5 5 5" stroke="#333" stroke-width="2" fill="none"/></svg></div>
<div class="arrow-btn" style="left:1138px"><svg width="28" height="28"><path d="M12 9l5 5-5 5" stroke="#333" stroke-width="2" fill="none"/></svg></div>

<div class="sale" style="left:103px">
  <div class="head">Sold by Maya Reid 0400 112 358</div>
  <div class="photo" role="img" aria-label="Photo of a bright dining and living room" style="background:linear-gradient(180deg,#e9ecec,#9aa0a2)"></div>
  <div class="price">$670,000 &nbsp;FOR SALE</div>
  <div class="loc"><span style="color:var(--teal)">⚲</span><span>13/48 Wattle Street KENSINGTON NSW</span></div>
  <div class="feat">
    <span><svg width="18" height="10"><rect x="0" y="4" width="18" height="4" fill="var(--icon)"/><rect x="0" y="0" width="3" height="10" fill="var(--icon)"/></svg>1</span>
    <span><svg width="16" height="12"><rect x="0" y="5" width="16" height="5" rx="2" fill="var(--icon)"/><rect x="1" y="0" width="2" height="6" fill="var(--icon)"/></svg>1</span>
    <span><svg width="18" height="12"><rect x="0" y="4" width="18" height="6" rx="2" fill="var(--icon)"/><rect x="3" y="0" width="12" height="6" rx="2" fill="var(--icon)"/></svg>1</span>
  </div>
</div>
<div class="sale" style="left:440px">
  <div class="head">Modern Apartment Close to All Amenities</div>
  <div class="photo" role="img" aria-label="Photo of a modern apartment lounge" style="background:linear-gradient(180deg,#eceeee,#a4a7a8)"></div>
  <div class="price">$609,000 &nbsp;FOR SALE</div>
  <div class="loc"><span style="color:var(--teal)">⚲</span><span>C402/4 Hollis Street CAMPSIE NSW</span></div>
  <div class="feat">
    <span><svg width="18" height="10"><rect x="0" y="4" width="18" height="4" fill="var(--icon)"/><rect x="0" y="0" width="3" height="10" fill="var(--icon)"/></svg>2</span>
    <span><svg width="16" height="12"><rect x="0" y="5" width="16" height="5" rx="2" fill="var(--icon)"/><rect x="1" y="0" width="2" height="6" fill="var(--icon)"/></svg>2</span>
    <span><svg width="18" height="12"><rect x="0" y="4" width="18" height="6" rx="2" fill="var(--icon)"/><rect x="3" y="0" width="12" height="6" rx="2" fill="var(--icon)"/></svg>1</span>
  </div>
</div>
<div class="sale" style="left:777px">
  <div class="head">Great Apartment for Investment</div>
  <div class="photo" role="img" aria-label="Photo of a warm furnished living room" style="background:linear-gradient(180deg,#d4a066,#7a4a2c)"></div>
  <div class="price">$500,000 &nbsp;FOR SALE</div>
  <div class="loc"><span style="color:var(--teal)">⚲</span><span>6/41 Belmore Street ASHFIELD NSW</span></div>
  <div class="feat">
    <span><svg width="18" height="10"><rect x="0" y="4" width="18" height="4" fill="var(--icon)"/><rect x="0" y="0" width="3" height="10" fill="var(--icon)"/></svg>1</span>
    <span><svg width="16" height="12"><rect x="0" y="5" width="16" height="5" rx="2" fill="var(--icon)"/><rect x="1" y="0" width="2" height="6" fill="var(--icon)"/></svg>1</span>
    <span><svg width="18" height="12"><rect x="0" y="4" width="18" height="6" rx="2" fill="var(--icon)"/><rect x="3" y="0" width="12" height="6" rx="2" fill="var(--icon)"/></svg>1</span>
  </div>
</div>

<section class="cta">
  <h2>Check to see if your property is<br>eligible for the propper sevice</h2>
  <div class="search" style="left:348px;top:192px"><div class="field">Search by Suburb</div><div class="go">Check Location</div></div>
</section>

<h2 class="section-title" style="top:3380px">Latest News</h2>
<article class="news" style="left:107px"><div class="photo" role="img" aria-label="Photo of a brick apartment block" style="background:linear-gradient(180deg,#a9c4dc,#8a6b4e)"></div><h3>First Home Buyers Guide - What to<br>look for</h3><div class="meta"><span><svg width="11" height="11"><rect width="11" height="11" rx="1" fill="var(--icon)"/><rect x="1" y="3" width="9" height="7" fill="#fff"/></svg>Jan 17, 2019</span><span><svg width="10" height="11"><circle cx="5" cy="3" r="3" fill="var(--icon)"/><path d="M0 11a5 5 0 0110 0z" fill="var(--icon)"/></svg>Harborkey Estate Agents</span></div></article>
<article class="news" style="left:442px"><div class="photo" role="img" aria-label="Photo of a sandstone apartment building" style="background:linear-gradient(180deg,#bcd3e6,#b7a27d)"></div><h3>47 Carrow Parade, Rosebery -<br>Auction Day</h3><div class="meta"><span><svg width="11" height="11"><rect width="11" height="11" rx="1" fill="var(--icon)"/><rect x="1" y="3" width="9" height="7" fill="#fff"/></svg>March 21, 2017</span><span><svg width="10" height="11"><circle cx="5" cy="3" r="3" fill="var(--icon)"/><path d="M0 11a5 5 0 0110 0z" fill="var(--icon)"/></svg>Harborkey Estate Agents</span></div></article>
<article class="news" style="left:775px"><div class="photo" role="img" aria-label="Photo of a park in front of apartments" style="background:linear-gradient(180deg,#a7c7e3,#6f9b55)"></div><h3>Eastlakes Community Fair Eastlakes<br>Community Fair</h3><div class="meta"><span><svg width="11" height="11"><rect width="11" height="11" rx="1" fill="var(--icon)"/><rect x="1" y="3" width="9" height="7" fill="#fff"/></svg>Sep 14, 2016</span><span><svg width="10" height="11"><circle cx="5" cy="3" r="3" fill="var(--icon)"/><path d="M0 11a5 5 0 0110 0z" fill="var(--icon)"/></svg>Harborkey Estate Agents</span></div></article>

<section class="contact">
  <h2>Contact Us</h2>
  <div class="input" style="left:107px;top:151px;width:238px;height:49px">Your Name</div>
  <div class="input" style="left:353px;top:151px;width:238px;height:49px">Emaill</div>
  <div class="input" style="left:598px;top:151px;width:238px;height:49px">Phone No</div>
  <div class="input" style="left:843px;top:151px;width:238px;height:49px;font-size:13px">Service Area<span style="float:right">⌄</span></div>
  <div class="input" style="left:107px;top:214px;width:974px;height:95px">Comments / Questions</div>
  <div class="submit">SUBMIT NOW &nbsp;➔</div>
</section>

<footer class="footer">
  <div class="brand" style="top:72px;left:107px"><i></i>Harborkey</div>
  <div class="row" style="top:146px"><div class="circle"><svg width="14" height="18" viewBox="0 0 14 18"><path d="M7 0a7 7 0 017 7c0 5-7 11-7 11S0 12 0 7a7 7 0 017-7z" fill="var(--teal)"/><circle cx="7" cy="7" r="2.5" fill="#fff"/></svg></div><span>Shop 4, 88 Wharf Lane, Mascot<br>NSW 2020</span></div>
  <div class="row" style="top:210px"><div class="circle"><svg width="14" height="14" viewBox="0 0 24 24"><path fill="var(--teal)" d="M6.6 10.8a15 15 0 006.6 6.6l2.2-2.2c.3-.3.7-.4 1-.2 1.1.4 2.3.6 3.6.6.6 0 1 .4 1 1V20c0 .6-.4 1-1 1A17 17 0 013 4c0-.6.4-1 1-1h3.5c.6 0 1 .4 1 1 0 1.3.2 2.5.6 3.6.1.3 0 .7-.2 1z"/></svg></div><span>02 9000 4821</span></div>
  <div class="row" style="top:272px"><div class="circle"><svg width="16" height="12" viewBox="0 0 16 12"><rect x="1" y="1" width="14" height="10" fill="none" stroke="var(--teal)" stroke-width="2"/><path d="M1 1l7 6 7-6" stroke="var(--teal)" stroke-width="2" fill="none"/></svg></div><span>ENQUIRIES@HARBORKEYHOMES.COM.AU</span></div>
  <h5 style="left:423px;top:80px">Quick Links</h5>
  <ul class="links"><li>Home</li><li>About Us</li><li>Recent Listings</li><li>Reviews</li><li>Contact us</li></ul>
  <h5 style="left:592px;top:80px">Get in Touch</h5>
  <div class="hours"><div><b>Monday - Friday</b>: &nbsp;9am - 6pm</div><div><b>Saturday</b>: &nbsp;9am - 3pm</div><div><b>Sunday</b>: &nbsp;Closed</div></div>
  <div class="map" role="img" aria-label="Street map showing the office location in Mascot"></div>
</footer>
<div class="copy">Copyright © 2021 Harborkey Estate Agent. All Rights Reserved</div>

</body>
</html>
```